NEW Gummy line needs fabulous, eye catching, juicy packaging!

***PLEASE NOTE: this is ONE bag, with THREE FLAVORS in the one bag. We are looking for a design that visually represents the three flavors in the bag*****

We are a well established cannabis company in Washington State, looking to launch a new line of gummies that are more affordable for the marketplace as people struggle with rising prices. The new brand name is "Tinsel & Company" and the product will be called "Lantern Meadow" - every bag is a MULTI-FLAVOR pack of 3 flavors (Washington State Cherry, Blue Elderberry, Royal Purple Raspberry) and an example of the gummy berry shape has been uploaded. We are looking for the packaging to reflect the three fruit flavors inside the bag - and can also have images of the shape of the gummies inside - I will upload an example of the gummy shape for reference also.

There are a number of "required elements" for state compliance in our state, so I will upload an example of our current 'VOLTA' brand APPLE flavor packaging so you can see how those "required elements" appear (Not for Kids icon, 21+ icon, the weight, the serving size information, 100mg THC/bag, and all the warning language is the same for this product as the APPLE example bag I have uploaded). Please reference the APPLE packaging for the icons and copy ONLY - this contest is for Tinsel & Company which is a new brand and we would like to see completely new concepts as both brands will be sold in the same stores.

We are most concerned with the visual concept - so no need to get all the placements, or all of the required elements for this initial contest, we can work together to perfect it once chosen. But in past competitions, designers have found it helpful to know for placement.

***NO CANNABIS IMAGERY PLEASE***

The products are sold in specialty dispensaries so customers are aware the products contain THC. We are more so looking for retail packaging that is trendy, modern, eye catching and enticing for a gummy food product.

**I have also uploaded a "PIPWICKS" package and a "ZUNK" - they are competitors - so we don't want to look like them, but providing it for inspiration where they mix the candy and the fruit, which can also be an idea for us.

PLEASE NOTE: This is a one bag design - each bag contains three flavors. So the design should reflect an mix of the 3 berry flavors

I am extending the deadline as we were able to push our print deadline back and I would like to give designers the weekend for their submissions. I also clarified the brief - ONE BAG, 3 FLAVORS inside - and hoping this is helpful for the designers also.

Target Market(s)

21+ THC Gummy lovers in Washington state

Industry/Entity Type

Cannabis Edibles

Requirements
Must have
• BOLD, eye catching, delicious design that is appealing for a gummy product (berries and product image a PLUS)
Nice to have
• incorporate the berries as visual, orchard visuals, organic but vibrant and juicy and fun
Should not have
• NO CANNABIS IMAGERY PLS

```html
<!DOCTYPE html>
<html lang="en">
<head>
<meta charset="utf-8">
<title>Lantern Meadow Gummies Pouch</title>
<link href="https://fonts.googleapis.com/css2?family=Josefin+Sans:wght@700&family=Poppins:wght@500;600;700&display=swap" rel="stylesheet">
<style>
  :root {
    --stage: #e4e4e6;
    --plum-dark: #34172f;
    --plum: #4a1c41;
    --magenta: #c8186d;
    --magenta-deep: #a3145a;
    --pink-band: #d42a78;
    --cream: #f6ecee;
    --soft-text: #d9c3d2;
    --berry-red: #c2324a;
    --berry-dark: #3a1f3e;
  }
  * { margin: 0; padding: 0; box-sizing: border-box; }
  html, body { width: 1200px; height: 900px; overflow: hidden; }
  body {
    background: var(--stage);
    position: relative;
    font-family: "Poppins", sans-serif;
  }
  .pouch {
    position: absolute;
    left: 330px; top: 40px;
    width: 540px; height: 820px;
    border-radius: 26px 26px 34px 34px;
    overflow: hidden;
    background: linear-gradient(180deg, var(--plum-dark) 0%, var(--plum) 14%, #7a1d5a 30%, var(--magenta-deep) 45%, var(--magenta) 62%, var(--magenta) 100%);
    text-align: center;
    color: var(--cream);
  }
  .brand {
    position: absolute; top: 108px; left: 0; right: 0;
    font-family: "Poppins", sans-serif;
    font-weight: 700;
    font-size: 30px;
    line-height: 1.1;
    color: var(--cream);
  }
  .product-name {
    position: absolute; top: 200px; left: 0; right: 0;
    font-family: "Josefin Sans", sans-serif;
    font-weight: 700;
    font-size: 84px;
    line-height: 1.08;
    letter-spacing: 2px;
    color: var(--cream);
  }
  .product-type {
    position: absolute; top: 402px; left: 0; right: 0;
    font-family: "Josefin Sans", sans-serif;
    font-weight: 700;
    font-size: 25px;
    line-height: 1.3;
    letter-spacing: 1.5px;
    color: var(--cream);
  }
  .product-art {
    position: absolute; top: 480px; left: 30px;
    width: 440px; height: 170px;
    border-radius: 60px 60px 20px 20px;
    background: linear-gradient(90deg, var(--berry-red) 0%, #d8596a 30%, #8f3a3a 50%, #e06a6a 70%, var(--berry-red) 100%);
  }
  .base {
    position: absolute; left: 0; top: 0; width: 540px; height: 820px;
  }
  .flavor-band {
    position: absolute; top: 665px; left: 60px;
    width: 340px; height: 74px;
    background: var(--pink-band);
    border-radius: 6px;
  }
  .flavor-band strong {
    display: block; padding-top: 8px;
    font-weight: 700; font-size: 24px; line-height: 1.2;
  }
  .flavor-band span {
    display: block; font-weight: 500; font-size: 18px; line-height: 1.3;
  }
  .dose-badge {
    position: absolute; top: 605px; left: 388px;
    width: 132px; height: 132px;
    border-radius: 50%;
    background: var(--magenta-deep);
    display: flex; flex-direction: column; align-items: center; justify-content: center;
    font-weight: 600;
  }
  .dose-badge .unit { font-size: 20px; line-height: 1; }
  .dose-badge .amount { font-size: 40px; font-weight: 700; line-height: 1.05; }
  .dose-badge .note { font-size: 13px; line-height: 1.15; }
  .flavor-list {
    position: absolute; top: 756px; left: 0; right: 0;
    font-size: 13px; font-weight: 500; line-height: 1.35;
    color: var(--soft-text);
  }
  .net-weight {
    position: absolute; top: 793px; left: 0; right: 0;
    font-size: 15px; font-weight: 600;
    color: var(--soft-text);
  }
</style>
</head>
<body>
  <main class="pouch">
    <svg class="base" viewBox="0 0 540 820" aria-hidden="true">
      <path d="M0 640 Q270 560 540 640 L540 820 L0 820 Z" fill="var(--berry-dark)"/>
      <rect x="0" y="0" width="540" height="10" fill="#2a1226"/>
    </svg>
    <div class="brand">Tinsel<br>&amp; Company</div>
    <h1 class="product-name">LANTERN<br>MEADOW</h1>
    <p class="product-type">CANNABIS INFUSED<br>GUMMIES</p>
    <div class="product-art" role="img" aria-label="Pile of berry-shaped gummies with blackberries, raspberries and a strawberry"></div>
    <div class="flavor-band">
      <strong>3 Berry Flavors</strong>
      <span>in Every Bag</span>
    </div>
    <div class="dose-badge">
      <span class="unit">MG</span>
      <span class="amount">100</span>
      <span class="note">THC<br>PER BAG</span>
    </div>
    <p class="flavor-list">Washington Cherry - Blue Elderberry<br>Royal Purple Raspberry</p>
    <p class="net-weight">NET WT 0.7 OZ (20 G)</p>
  </main>
</body>
</html>
```